Business Card Design & Logo Design

Im a new company selling: balloons, bespoke gift wrapping services & Christmas decorating services i.e. I will come and decorate your tree, wrap your xmas presents, set & decorate your dining table, help you host your xmas party etc. etc.

I don't do 'cheesey' stuff so need a sophisticated card.

I love b&w colours, I love stripes and smart looking stuff.

I do already have an idea and if I don't find anything else then I will go with my idea but would then just need somebody to create the artwork for me.

www.copperwillow.co.uk is currently in the process of being designed so any ideas of logos/designs must also work with a website.

Industry/Entity Type

Business

Contact Information for Business Card

Copper Willow
Hollowmere upon Ash
KT14 9RD
Marlowshire
01632 960418
or
07700 900736

treats@copperwillow.co.uk

```html
<!DOCTYPE html>
<html lang="en">
<head>
<meta charset="utf-8">
<title>Copper Willow – Business Card Options</title>
<link rel="stylesheet" href="https://fonts.googleapis.com/css2?family=Federo&family=Questrial&display=swap">
<style>
  :root {
    --sheet: #ffffff;
    --option-number: #333333;
    --ink-dark: #2b2a29;
    --pink: #e4137b;
    --pink-light: #f7b3d6;
    --pink-deep: #c20a66;
    --text-light: #ffffff;
    --text-dark: #2b2a29;
    --mono-pattern-a: #e6e6e6;
    --mono-pattern-b: #9a9a9a;
    --blue-pattern-a: #e8f5fc;
    --blue-pattern-b: #3fa9e0;
    --blue-panel-light: #ffffff;
    --blue-panel: #8fd0f1;
    --card-edge: #d9d9d9;
  }
  * { box-sizing: border-box; margin: 0; padding: 0; }
  html, body { width: 763px; height: 1200px; overflow: hidden; background: var(--sheet); }
  .sheet { position: relative; width: 763px; height: 1200px; }

  .option-number {
    position: absolute; left: 52px;
    font: 22px "Questrial", Arial, sans-serif; color: var(--option-number);
  }

  .card {
    position: absolute; left: 108px; width: 537px; height: 316px;
    overflow: hidden; border: 1px solid var(--card-edge);
  }
  .card--one   { top: 42px; }
  .card--two   { top: 410px; }
  .card--three { top: 782px; }

  .pattern-top, .pattern-side { position: absolute; }
  .pattern-top  { left: 0; top: 0; width: 100%; height: 94px; }
  .pattern-side { left: 462px; top: 94px; width: 75px; bottom: 0; }
  .pattern--mono { background: linear-gradient(135deg, var(--mono-pattern-a), var(--mono-pattern-b) 60%, var(--mono-pattern-a)); }
  .pattern--blue { background: linear-gradient(135deg, var(--blue-pattern-a), var(--blue-pattern-b) 60%, var(--blue-pattern-a)); }

  .info-panel {
    position: absolute; left: 0; top: 94px; width: 448px; bottom: 0;
    background: var(--ink-dark); color: var(--text-light);
  }
  .info-panel--light {
    background: radial-gradient(ellipse at 60% 35%, var(--blue-panel-light) 0%, var(--blue-panel) 85%);
    color: var(--text-dark);
  }

  .ribbon-horizontal {
    position: absolute; left: 0; top: 90px; width: 100%; height: 9px;
    background: linear-gradient(90deg, var(--pink) 0%, var(--pink) 60%, var(--pink-light) 72%, var(--pink) 85%, var(--pink-light) 95%, var(--pink) 100%);
  }
  .ribbon-vertical {
    position: absolute; left: 448px; top: 0; width: 14px; height: 100%;
    background: linear-gradient(90deg, var(--pink-deep), var(--pink-light) 45%, var(--pink) 100%);
  }
  .bow {
    position: absolute; left: 438px; top: 70px; width: 66px; height: 66px;
    background: radial-gradient(circle at 40% 40%, var(--pink-light), var(--pink) 70%);
    border-radius: 40% 50% 45% 50%;
  }

  .business-name {
    position: absolute; left: 0; width: 458px; top: 12px; text-align: center;
    font: 36px "Federo", Georgia, serif; color: var(--pink);
  }
  .contact-list { position: absolute; left: 101px; top: 66px; list-style: none;
    font: 18px "Questrial", Arial, sans-serif; line-height: 28.5px; }
  .contact-list li { position: relative; }
  .contact-icon { position: absolute; left: -24px; width: 14px; height: 14px; }
  .contact-icon--phone { top: 24px; }
  .contact-icon--mail { top: 8px; }
  .address {
    position: absolute; left: 0; width: 448px; top: 176px; text-align: center;
    font: 17px "Questrial", Arial, sans-serif; white-space: nowrap;
  }
</style>
</head>
<body>
<main class="sheet">

  <span class="option-number" style="top:150px">1</span>
  <section class="card card--one" aria-label="Business card option 1">
    <div class="pattern-top pattern--mono" role="img" aria-label="Black and white damask pattern"></div>
    <div class="pattern-side pattern--mono" role="img" aria-label="Black and white damask pattern"></div>
    <div class="info-panel">
      <h1 class="business-name">Copper Willow</h1>
      <ul class="contact-list">
        <li>01632 960418
          <svg class="contact-icon contact-icon--phone" viewBox="0 0 14 14"><path d="M3 1 L5 4 L4 5.5 Q5.5 8.5 8.5 10 L10 9 L13 11 L11.5 13 Q5 12.5 1 3 Z" fill="var(--pink)"/></svg>
        </li>
        <li>07700 900736</li>
        <li>treats@copperwillow.co.uk
          <svg class="contact-icon contact-icon--mail" viewBox="0 0 14 14"><rect x="1" y="3" width="12" height="8" fill="none" stroke="var(--pink)" stroke-width="1.3"/><path d="M1 3 L7 8 L13 3" fill="none" stroke="var(--pink)" stroke-width="1.3"/></svg>
        </li>
      </ul>
      <p class="address">Hollowmere&nbsp; upon Ash KT14 9RD Marlowshire</p>
    </div>
    <div class="ribbon-horizontal"></div>
    <div class="ribbon-vertical"></div>
    <div class="bow" role="img" aria-label="Pink satin ribbon bow"></div>
  </section>

  <span class="option-number" style="top:544px">2</span>
  <section class="card card--two" aria-label="Business card option 2">
    <div class="pattern-top pattern--mono" role="img" aria-label="Black leaf and swirl pattern on white"></div>
    <div class="pattern-side pattern--mono" role="img" aria-label="Black leaf and swirl pattern on white"></div>
    <div class="info-panel">
      <h1 class="business-name">Copper Willow</h1>
      <ul class="contact-list">
        <li>01632 960418
          <svg class="contact-icon contact-icon--phone" viewBox="0 0 14 14"><path d="M3 1 L5 4 L4 5.5 Q5.5 8.5 8.5 10 L10 9 L13 11 L11.5 13 Q5 12.5 1 3 Z" fill="var(--pink)"/></svg>
        </li>
        <li>07700 900736</li>
        <li>treats@copperwillow.co.uk
          <svg class="contact-icon contact-icon--mail" viewBox="0 0 14 14"><rect x="1" y="3" width="12" height="8" fill="none" stroke="var(--pink)" stroke-width="1.3"/><path d="M1 3 L7 8 L13 3" fill="none" stroke="var(--pink)" stroke-width="1.3"/></svg>
        </li>
      </ul>
      <p class="address">Hollowmere&nbsp; upon Ash KT14 9RD Marlowshire</p>
    </div>
    <div class="ribbon-horizontal"></div>
    <div class="ribbon-vertical"></div>
    <div class="bow" role="img" aria-label="Pink satin ribbon bow"></div>
  </section>

  <span class="option-number" style="top:936px">3</span>
  <section class="card card--three" aria-label="Business card option 3">
    <div class="pattern-top pattern--blue" role="img" aria-label="Blue leaf and swirl pattern on white"></div>
    <div class="pattern-side pattern--blue" role="img" aria-label="Blue leaf and swirl pattern on white"></div>
    <div class="info-panel info-panel--light">
      <h1 class="business-name">Copper Willow</h1>
      <ul class="contact-list">
        <li>01632 960418
          <svg class="contact-icon contact-icon--phone" viewBox="0 0 14 14"><path d="M3 1 L5 4 L4 5.5 Q5.5 8.5 8.5 10 L10 9 L13 11 L11.5 13 Q5 12.5 1 3 Z" fill="var(--pink)"/></svg>
        </li>
        <li>07700 900736</li>
        <li>treats@copperwillow.co.uk
          <svg class="contact-icon contact-icon--mail" viewBox="0 0 14 14"><rect x="1" y="3" width="12" height="8" fill="none" stroke="var(--pink)" stroke-width="1.3"/><path d="M1 3 L7 8 L13 3" fill="none" stroke="var(--pink)" stroke-width="1.3"/></svg>
        </li>
      </ul>
      <p class="address">Hollowmere&nbsp; upon Ash KT14 9RD Marlowshire</p>
    </div>
    <div class="ribbon-horizontal"></div>
    <div class="ribbon-vertical"></div>
    <div class="bow" role="img" aria-label="Pink satin ribbon bow"></div>
  </section>

</main>
</body>
</html>
```